Delia Morvan
exclusive handcrafted jewelry
Simple
delmorvan@quillbox.net
deliamorvandesign.net
business card should be shaded black like uploaded logo.
I also like the royal blue option !
I have no idea what is on that file since I can not open it . I hope it is my logo in blue or shaded black.

```html
<!DOCTYPE html>
<html lang="en">
<head>
<meta charset="utf-8">
<title>Delia Morvan – Envelope Options</title>
<link rel="stylesheet" href="https://fonts.googleapis.com/css2?family=Cormorant+Garamond:ital,wght@0,500;1,500&display=swap">
<style>
  :root{
    --backdrop:#e9e6e1;
    --paper:#ffffff;
    --navy:#24224f;
    --navy-deep:#121130;
    --navy-glow:#3a3878;
    --black:#0b0b0d;
    --ink:#1b1b22;
    --muted:#8b8b95;
    --label:#4a4a4a;
  }
  *{box-sizing:border-box;margin:0;padding:0}
  html,body{width:1200px;height:391px;overflow:hidden;background:var(--backdrop)}
  body{position:relative;font-family:"Cormorant Garamond",Georgia,serif;color:var(--ink)}

  .brand-header{position:absolute;top:6px;left:0;width:100%;text-align:center;line-height:1}
  .brand-header .name{font-size:17px;font-weight:500;color:var(--ink)}
  .brand-header .tag{display:block;font-size:8px;font-style:italic;color:var(--muted);margin-top:2px}

  .option{position:absolute;top:44px;width:288px;height:340px}
  .option-label{position:absolute;top:0;left:2px;font-size:9px;color:var(--label)}

  .envelope{position:absolute;top:12px;left:0;width:288px;height:328px;box-shadow:0 2px 6px rgba(0,0,0,.18)}
  .flap-top,.body,.flap-bottom{position:absolute;left:0;width:100%}
  .flap-top{top:0;height:56px;clip-path:polygon(8% 0,92% 0,100% 100%,0 100%)}
  .body{top:56px;height:136px;background:var(--paper);overflow:hidden}
  .flap-bottom{top:192px;height:136px;clip-path:polygon(0 0,100% 0,93% 100%,7% 100%)}

  .navy{background:radial-gradient(ellipse at 50% 30%,var(--navy-glow),var(--navy) 55%,var(--navy-deep))}
  .black{background:linear-gradient(180deg,#1c1c20,var(--black))}
  .white{background:var(--paper);border-bottom:1px solid #ddd}

  .flap-mark{position:absolute;left:0;width:100%;text-align:center;font-size:13px;font-weight:500;color:#fff}
  .flap-top .flap-mark{top:20px}
  .flap-bottom .flap-mark{top:18px}
  .white .flap-mark{color:var(--ink)}

  .sender{position:absolute;top:14px;left:14px;line-height:1}
  .sender .name{font-size:16px;font-weight:500;color:var(--ink)}
  .sender .tag{display:block;font-size:7px;font-style:italic;color:var(--muted);margin-top:2px}
  .sender .contact{display:block;font-size:6px;color:var(--muted);margin-top:3px}

  .swoosh{position:absolute;left:0;bottom:0;width:100%;height:44px}

  .band{position:absolute;left:0;bottom:10px;width:100%;height:8px;background:var(--navy);color:#c9c8e6;font-size:5.5px;text-align:center;line-height:8px}

  .faint-name{position:absolute;right:18px;bottom:22px;font-size:24px;font-weight:500;color:#d6d6da}
  .flap-bottom.split{background:var(--paper)}
  .flap-bottom.split .band-top{position:absolute;top:0;left:0;width:100%;height:32px;background:radial-gradient(ellipse at 50% 0,var(--navy-glow),var(--navy) 60%,var(--navy-deep))}
</style>
</head>
<body>
  <header class="brand-header">
    <span class="name">Delia Morvan</span>
    <span class="tag">exclusive handcrafted jewelry</span>
  </header>

  <!-- Option 1 -->
  <section class="option" style="left:12px">
    <span class="option-label">Example 1</span>
    <div class="envelope">
      <div class="flap-top navy"><span class="flap-mark">Delia Morvan</span></div>
      <div class="body">
        <div class="sender"><span class="name">Delia Morvan</span><span class="tag">exclusive handcrafted jewelry</span></div>
        <svg class="swoosh" viewBox="0 0 288 44" preserveAspectRatio="none" aria-hidden="true">
          <path d="M0 44 L0 20 Q150 40 288 4 L288 44 Z" fill="var(--navy)"/>
        </svg>
      </div>
      <div class="flap-bottom split">
        <div class="band-top"></div>
        <span class="faint-name">Delia Morvan</span>
      </div>
    </div>
  </section>

  <!-- Option 2 -->
  <section class="option" style="left:308px">
    <span class="option-label">Example 2</span>
    <div class="envelope">
      <div class="flap-top navy"><span class="flap-mark">Delia Morvan</span></div>
      <div class="body">
        <div class="sender"><span class="name">Delia Morvan</span><span class="tag">exclusive handcrafted jewelry</span></div>
        <div class="band">delmorvan@quillbox.net · deliamorvandesign.net</div>
      </div>
      <div class="flap-bottom navy"><span class="flap-mark">Delia Morvan</span></div>
    </div>
  </section>

  <!-- Option 3 -->
  <section class="option" style="left:604px">
    <span class="option-label">Example 3</span>
    <div class="envelope">
      <div class="flap-top black"><span class="flap-mark">Delia Morvan</span></div>
      <div class="body">
        <div class="sender"><span class="name">Delia Morvan</span><span class="tag">exclusive handcrafted jewelry</span><span class="contact">delmorvan@quillbox.net · deliamorvandesign.net</span></div>
      </div>
      <div class="flap-bottom black"><span class="flap-mark">Delia Morvan</span></div>
    </div>
  </section>

  <!-- Option 4 -->
  <section class="option" style="left:900px">
    <span class="option-label">Example 4</span>
    <div class="envelope">
      <div class="flap-top white"><span class="flap-mark">Delia Morvan</span></div>
      <div class="body">
        <div class="sender"><span class="name">Delia Morvan</span><span class="tag">exclusive handcrafted jewelry</span></div>
        <div class="band">delmorvan@quillbox.net · deliamorvandesign.net</div>
      </div>
      <div class="flap-bottom navy"><span class="flap-mark">Delia Morvan</span></div>
    </div>
  </section>
</body>
</html>
```